依頼詳細
屋外にタペストリーで掲げている店案内ですが、ショッピングセンター内にあるため屋外からエステだと一目でわかるものにしたいと考えております。そのためのデザインをお願いいたします。
記載項目
記載項目
特にエステティックであることをはっきりと掲載したいため「ロゴマーク」「エステティックサロン」「美顔」「痩身」「脱毛」というワードを大きく
続いて「電話番号」「営業時間」
また「店名」も掲載しますが目立たなくとも良いです。
ロゴマークは添付のものをご利用ください。
色ならびにロゴマーク中のグラデーションの変更はしないようにお願いいたします。
参考として旧タペストリーと他店の駐車場看板を添付します。
旧タペストリーのデザインとは全くかけ離れて構いません。
駐車場看板は見せ方の参考として添付します。店名よりもエステティックを強調しているという事の参考になればと思います。

店名 ルフィナ鯖江店
電話番号 0778-41-6093
営業時間 9:30~20:30
サイズ:縦2400mm×横3200mm
希望イメージ
シンプル 複雑
単色 カラフル
暗い 明るい
日常 高級
遊び心 厳粛
未来的 伝統的
女性的 男性的
希望する色
設定なし
納品ファイル
• イラストレーター形式 (.ai)
• フォトショップ形式 (.psd)
補足説明
写真利用の場合は、納品の際は埋め込みではなくリンクでお願いします。
表記につきまして若干変更をさせていただきます、

「エステティックサロン」は英字よりカナ表記が目立つようにお願いいたします。
「美顔」→「フェイシャル」に変更(カナ表記)
「痩身」→「ボディ」に変更(カナ表記)
「脱毛」→変更なし

また女性の画像等はイメージやパーツとして使用いただいてもOKですが、スワンのマークをもう少し前面に出していただけたらと思います。
画像のイメージが前面にでるより、スワンのロゴが前面にでるようにできればと思います。イメージ画像等は全くないものでも可です。

添付でスワンのロゴのみのaiを追加いたします。

締め切りを変更させていただきます。

当方が伝えたいものが、しっかりと出ていて、色味も落ち着きがありながらロゴがはっきりと見えるデザインで好感が持てました。

本当にたくさんのデザインを頂きありがとうございます。

```html
<!DOCTYPE html>
<html lang="ja">
<head>
<meta charset="utf-8">
<title>エステティックサロン RUFINA</title>
<link href="https://fonts.googleapis.com/css2?family=Noto+Sans+JP:wght@400;700;900&family=Noto+Serif+JP:wght@700&family=Encode+Sans+Semi+Condensed:wght@400&display=swap" rel="stylesheet">
<style>
  :root {
    --rose: #e0566f;
    --rose-soft: #e8718a;
    --crimson: #b8123f;
    --silk-light: #f6d3dc;
    --ink: #333333;
    --label: #555555;
    --footer: #5b5858;
    --white: #ffffff;
  }
  html, body { margin: 0; padding: 0; overflow: hidden; }
  .banner {
    position: relative;
    width: 1200px;
    height: 900px;
    overflow: hidden;
    background: var(--white);
    font-family: "Noto Sans JP", sans-serif;
  }
  .silk-backdrop {
    position: absolute;
    left: 0; top: 180px;
    width: 1200px; height: 626px;
    background:
      radial-gradient(ellipse 520px 260px at 330px 200px, rgba(255,255,255,0.95), rgba(255,255,255,0) 70%),
      radial-gradient(ellipse 700px 380px at 1050px 420px, var(--crimson), rgba(184,18,63,0) 75%),
      linear-gradient(160deg, var(--white) 0%, var(--silk-light) 35%, var(--rose-soft) 62%, #c7355c 85%, #f3c6d2 100%);
  }
  .silk-backdrop::before {
    content: "";
    position: absolute;
    left: 0; top: -120px; width: 1200px; height: 240px;
    background: linear-gradient(to bottom, var(--white) 55%, rgba(255,255,255,0));
  }
  .brand-mark {
    position: absolute;
    left: 92px; top: 200px;
    width: 150px; height: 150px;
    border-radius: 50%;
    background: var(--rose);
  }
  .category-title {
    position: absolute;
    left: 344px; top: 88px;
    margin: 0;
    font-size: 82px;
    font-weight: 900;
    letter-spacing: -1px;
    color: var(--rose);
    text-shadow: 4px 6px 8px rgba(0,0,0,0.35);
    white-space: nowrap;
  }
  .category-en {
    position: absolute;
    left: 348px; top: 190px;
    font-family: "Encode Sans Semi Condensed", sans-serif;
    font-size: 52px;
    color: var(--rose);
    white-space: nowrap;
  }
  .brand-name {
    position: absolute;
    left: 342px; top: 248px;
    font-family: "Encode Sans Semi Condensed", sans-serif;
    font-size: 150px;
    line-height: 1;
    color: var(--rose);
    letter-spacing: 2px;
  }
  .menu-item {
    position: absolute;
    width: 148px; height: 148px;
    margin: -74px 0 0 -74px;
    border-radius: 50%;
    background: radial-gradient(circle at 45% 40%, #ffffff 60%, #ededed 100%);
    box-shadow: 0 8px 14px rgba(0,0,0,0.3);
    display: flex; align-items: center; justify-content: center;
    font-size: 23px;
    color: var(--label);
  }
  .accent-dot {
    position: absolute;
    border-radius: 50%;
    background: var(--rose-soft);
    box-shadow: 2px 6px 10px rgba(0,0,0,0.3);
  }
  .tagline {
    position: absolute;
    left: 0; width: 1236px; top: 678px;
    margin: 0;
    text-align: center;
    font-family: "Noto Serif JP", serif;
    font-size: 34px;
    font-weight: 700;
    color: var(--ink);
    letter-spacing: 2px;
  }
  .shop-info {
    position: absolute;
    left: 0; top: 806px;
    width: 1200px; height: 94px;
    background: var(--footer);
    color: var(--white);
    font-weight: 700;
    font-size: 28px;
    display: flex; align-items: center;
  }
  .shop-info span { position: absolute; white-space: nowrap; }
  .shop-name { left: 44px; font-size: 30px; }
  .shop-phone { left: 322px; }
  .shop-hours { left: 768px; }
</style>
</head>
<body>
  <main class="banner">
    <div class="silk-backdrop" role="img" aria-label="流れるピンクのシルク生地の背景イメージ"></div>

    <div class="brand-mark" aria-hidden="true"></div>
    <h1 class="category-title">エステティックサロン</h1>
    <div class="category-en">Esthetic salon</div>
    <div class="brand-name">RUFINA</div>

    <div class="accent-dot" style="left:648px; top:452px; width:52px; height:52px;"></div>
    <div class="accent-dot" style="left:464px; top:590px; width:68px; height:68px;"></div>
    <div class="accent-dot" style="left:836px; top:660px; width:68px; height:68px;"></div>

    <div class="menu-item" style="left:450px; top:552px;">フェイシャル</div>
    <div class="menu-item" style="left:618px; top:552px;">ボディ</div>
    <div class="menu-item" style="left:780px; top:552px;">脱毛</div>

    <p class="tagline">貴女の奇麗が目覚める</p>

    <footer class="shop-info">
      <span class="shop-name">ルフィナ鯖江店</span>
      <span class="shop-phone">■電話番号：0778-41-6093</span>
      <span class="shop-hours">■営業時間：9:30 ～ 20:30</span>
    </footer>
  </main>
</body>
</html>
```